Business Card Design Project

This is to go hand in hand with our stationery project.
Target Market(s)
Business Professionals in the Finance, HR and C-Level management arena. They are global companies that run enterprise technology solutions/products.
Mostly Male, mid 30's to 60's.
Industry/Entity Type
Business
Font styles to use
Other font styles liked:
- Calibri
Colors
9bcb3c
000000
1b1b1b
c4c4c4
ffffff
Requirements
Must have
- Logo
Name, title, contact details, address on the front of the card.
ABN and web address need to be on the card, along with our tag line
See | Share | Do
We also require rounded corners and for the card to be landscape please.
Our green is
C98 M0 Y93 K0
Modern, contemporary and must have white space for people to write on.
Nice to have
- Consistent elements with the stationery design.
Should not have
- No 90's waves - We want the feeling of movement but no wavey lines.

```html
<!DOCTYPE html>
<html lang="en">
<head>
<meta charset="utf-8">
<title>NEXA Business Card</title>
<link rel="stylesheet" href="https://fonts.googleapis.com/css2?family=Open+Sans:wght@600;700&display=swap">
<style>
  :root {
    --green: #9bcb3c;
    --black: #000000;
    --charcoal: #333333;
    --title-grey: #3a3a3a;
    --light-grey: #c4c4c4;
    --white: #ffffff;
  }
  html, body {
    margin: 0;
    padding: 0;
    width: 1200px;
    height: 720px;
    overflow: hidden;
    background: var(--white);
  }
  .card-canvas {
    display: block;
    width: 1200px;
    height: 720px;
    font-family: "Open Sans", Calibri, sans-serif;
  }
  .card-base { fill: var(--light-grey); }
  .card-sweep { fill: var(--charcoal); }
  .card-band { fill: var(--white); }
  .person-name { fill: var(--black); font-size: 52px; font-weight: 700; }
  .person-title { fill: var(--title-grey); font-size: 52px; font-weight: 700; }
  .web-address { fill: var(--green); font-size: 26px; font-weight: 700; }
  .brand-name { fill: var(--white); font-size: 150px; font-weight: 700; letter-spacing: 4px; }
  .street-address { fill: var(--green); font-size: 26.5px; font-weight: 700; }
  .contact-line { fill: var(--black); font-size: 27.5px; font-weight: 700; }
  .contact-label { fill: var(--green); }
</style>
</head>
<body>
<svg class="card-canvas" viewBox="0 0 1145 683" preserveAspectRatio="none" xmlns="http://www.w3.org/2000/svg">
  <defs>
    <clipPath id="card-shape">
      <rect x="75" y="75" width="975" height="525" rx="45" ry="45"/>
    </clipPath>
    <clipPath id="sweep-shape">
      <path d="M 78 568 C 250 380 520 170 905 75 L 1050 75 L 1050 600 L 78 600 Z"/>
    </clipPath>
  </defs>

  <g class="card" clip-path="url(#card-shape)">
    <rect class="card-base" x="75" y="75" width="975" height="525"/>
    <g clip-path="url(#sweep-shape)">
      <rect class="card-sweep" x="75" y="75" width="975" height="525"/>
      <rect class="card-band" x="75" y="162" width="975" height="80"/>
      <rect class="card-band" x="75" y="520" width="975" height="80"/>
    </g>
  </g>

  <text class="person-name" x="445" y="200" text-anchor="end">DANIEL REEVE</text>
  <text class="person-title" x="445" y="255" text-anchor="end">Job Title</text>

  <text class="web-address" x="983" y="212" text-anchor="end">www.nexabusiness.com</text>

  <text class="brand-name" x="980" y="475" text-anchor="end">NEXA</text>

  <text class="street-address" x="562" y="553" text-anchor="middle">Level 7, 210 Harbour Road, Eastwood NSW 2122</text>
  <text class="contact-line" x="563" y="592" text-anchor="middle"><tspan class="contact-label">T:</tspan> + 61 2 5550 1842 <tspan dx="28" class="contact-label">F:</tspan> +61 2 5550 1843 <tspan dx="28" class="contact-label">ABN:</tspan> 12 345 678 901</text>
</svg>
</body>
</html>
```